Silverleaf upkeep services strata flyer

Looking for a flyer that will grab peoples attention also need to include some kind off promotional offer on there so they will hold onto the flyer . Would like approximateley 4 pictures of appartment blocks. Would like to include the following services. Building management Common area cleaning ,window cleaning, lawn mowing, gardening , pressure cleaning, carpet cleaning, bin cleaning. Handy man services.

Target Market(s)

appartment blocks/strata managers

Industry/Entity Type

Pressure Cleaning

Font styles to use
Serif

Colors
0355a3
ceddec
ec2027

Requirements
Must have
• company logo & colors contact details email: Info@silverleafupkeepservices.com.au
• Phone: 0438507721 website silverleafupkeepservices.com.au

```html
<!DOCTYPE html>
<html lang="en">
<head>
<meta charset="utf-8">
<title>Silverleaf Upkeep Services – Strata Flyer</title>
<link rel="stylesheet" href="https://fonts.googleapis.com/css2?family=Roboto+Slab:wght@700;800&family=Noto+Serif:wght@400;700&display=swap">
<style>
  :root {
    --title-blue: #1b4fd8;
    --offer-blue: #3b6fe0;
    --strip-blue: #d3e6f5;
    --swoosh-deep: #7ea9ee;
    --swoosh-light: #d6e9f7;
    --offer-red: #ec2027;
    --ink: #3d3d3d;
    --ink-dark: #2a2a2a;
    --paper: #ffffff;
    --photo-top: #6f9bd9;
    --photo-bottom: #c9d7e4;
  }
  * { margin: 0; padding: 0; box-sizing: border-box; }
  html, body { width: 846px; height: 1200px; overflow: hidden; background: var(--paper); }
  .flyer {
    position: relative;
    width: 846px;
    height: 1200px;
    background: var(--paper);
    font-family: "Noto Serif", Georgia, serif;
    color: var(--ink);
  }
  .brand-mark {
    position: absolute;
    left: 146px; top: 30px;
    width: 228px; height: 228px;
    border-radius: 50%;
    background: var(--title-blue);
  }
  .brand-title {
    position: absolute;
    left: 387px; top: 86px;
    font-family: "Roboto Slab", Georgia, serif;
    font-weight: 800;
    font-size: 52px;
    line-height: 46px;
    color: var(--title-blue);
    text-transform: uppercase;
    letter-spacing: 0.5px;
  }
  .swoosh { position: absolute; left: 0; top: 0; }
  .photo {
    position: absolute;
    left: 45px;
    width: 336px;
    background: linear-gradient(180deg, var(--photo-top) 0%, var(--photo-bottom) 100%);
  }
  .photo--tower { top: 295px; height: 239px; }
  .photo--estate { top: 536px; height: 239px; }
  .services {
    position: absolute;
    left: 434px; top: 350px;
  }
  .services__heading {
    font-family: "Roboto Slab", Georgia, serif;
    font-weight: 800;
    font-size: 21px;
    line-height: 28px;
    color: var(--title-blue);
    text-transform: uppercase;
    margin-bottom: 2px;
  }
  .services__list { list-style: none; }
  .services__item {
    position: relative;
    padding-left: 31px;
    font-size: 23.5px;
    line-height: 29px;
    color: var(--ink);
    white-space: nowrap;
  }
  .services__item::before {
    content: "";
    position: absolute;
    left: 3px; top: 12px;
    width: 6px; height: 6px;
    border-radius: 50%;
    background: var(--title-blue);
  }
  .offer {
    position: absolute;
    left: 0; top: 832px;
    width: 846px; height: 223px;
    background: var(--strip-blue);
    border-top: 4px dotted var(--ink-dark);
    border-bottom: 4px dotted var(--ink-dark);
  }
  .offer__brand {
    position: absolute;
    left: 60px; top: 50px;
    display: flex; align-items: center; gap: 12px;
  }
  .offer__mark {
    width: 110px; height: 110px;
    border-radius: 50%;
    background: var(--title-blue);
  }
  .offer__name {
    font-family: "Roboto Slab", Georgia, serif;
    font-weight: 800;
    font-size: 17px;
    line-height: 20px;
    color: var(--title-blue);
    text-transform: uppercase;
  }
  .offer__text {
    position: absolute;
    left: 280px; top: 26px;
    width: 456px;
    text-align: center;
  }
  .offer__title {
    font-family: "Noto Serif", Georgia, serif;
    font-weight: 700;
    font-size: 49px;
    line-height: 56px;
    color: var(--offer-red);
    text-transform: uppercase;
    white-space: nowrap;
  }
  .offer__call {
    font-weight: 700;
    font-size: 21px;
    line-height: 27px;
    color: var(--offer-blue);
    text-transform: uppercase;
    margin-top: 2px;
    white-space: nowrap;
  }
  .offer__terms {
    font-size: 18.5px;
    line-height: 25px;
    color: var(--ink-dark);
    margin-top: 6px;
  }
  .contact {
    position: absolute;
    left: 0; top: 1076px;
    width: 846px;
    text-align: center;
    font-size: 17.5px;
    line-height: 23px;
    color: var(--ink-dark);
  }
  .contact strong { font-weight: 700; }
</style>
</head>
<body>
<main class="flyer">
  <div class="brand-mark" aria-hidden="true"></div>
  <h1 class="brand-title">Silverleaf<br>Upkeep<br>Services</h1>

  <svg class="swoosh" width="846" height="1200" viewBox="0 0 846 1200" aria-hidden="true">
    <defs>
      <linearGradient id="swooshFill" x1="0" y1="0" x2="1" y2="0">
        <stop offset="0" stop-color="#7ea9ee"/>
        <stop offset="0.45" stop-color="#c4dcf4"/>
        <stop offset="1" stop-color="#d6e9f7"/>
      </linearGradient>
    </defs>
    <path d="M381 337 Q600 268 846 252 L846 801 Q600 800 381 740 Z" fill="url(#swooshFill)"/>
  </svg>

  <div class="photo photo--tower" role="img" aria-label="Photo of a modern apartment tower with balconies"></div>
  <div class="photo photo--estate" role="img" aria-label="Photo of apartment blocks behind a landscaped lawn"></div>

  <section class="services">
    <h2 class="services__heading">We can offer you:</h2>
    <ul class="services__list">
      <li class="services__item">Building management<br>common area cleaning</li>
      <li class="services__item">Window cleaning</li>
      <li class="services__item">Office cleaning</li>
      <li class="services__item">Pubs &amp; Clubs</li>
      <li class="services__item">Lawn mowing</li>
      <li class="services__item">Gardening</li>
      <li class="services__item">Pressure cleaning</li>
      <li class="services__item">Carpet cleaning</li>
      <li class="services__item">Bin cleaning</li>
      <li class="services__item">Handy man services</li>
    </ul>
  </section>

  <section class="offer">
    <div class="offer__brand">
      <div class="offer__mark" aria-hidden="true"></div>
      <div class="offer__name">Silverleaf<br>Upkeep<br>Services</div>
    </div>
    <div class="offer__text">
      <h2 class="offer__title">Special Offer!</h2>
      <p class="offer__call">Present this brochure<br>for your free initial clean!</p>
      <p class="offer__terms">Valid until 31-07-2015<br>Conditions Apply.</p>
    </div>
  </section>

  <footer class="contact">
    <p>silverleafupkeepservices.com.au</p>
    <p><strong>Email:</strong> Info@silverleafupkeepservices.com.au</p>
    <p><strong>Phone:</strong> 0438 507 721</p>
  </footer>
</main>
</body>
</html>
```